Permanent Makeup (cosmetics salon) Brochure

We need a 2-4 sites brochure for our Permanent Makeup (cosmetics salon). Our company is based in Austria / Vienna. -> Our homepage is www.mk-hollmeister.at
This brochure should show which treatments we provide ot our customers.

I've uploaded our old brochure, the content (text) would be nearly the same (look form "Must Haves", pics have to be new (look uploaded pics)
The old brochure is to dark. -> look for our homepage maybe you can make it like this

Target Market(s)

woman, age 25-70 years who wants to have permanent makeup on eyebrows, lips or eyeliner

Industry/Entity Type

Beauty Salon

Requirements
Must have
• pics which are uploaded.

*This text (somithing about our business)
"Für Frau Hollmeister ist Permanent Makeup ein Kunsthandwerk. Das Team von MK-Hollmeister ist spezialisiert auf natürliches Permanent Makeup damit der individuelle Typ jeder Kundin am schönsten zum Ausdruck kommt."

*We do this treatments: (english)
+ Augenbrauen Microblading (eyebrows)
+ Augenbrauen Permanent Makeup (eyebrows2)
+ Lidstrich Permanent Makeup (eyeliner)
+ Lip Blushing (lips)
+ Lippen Permanent Makeup (lips2)

* Our addresses (2 locations)
Wien
Lerchengasse 7b/21, 1080 Wien
Tel: 01/5826107

Villach
Birkenstraße 24, 9581 St. Ulrich
Tel: 0664/3158902

Mail: info@mk-hollmeister.at
www.mk-hollmeister.at

```html
<!DOCTYPE html>
<html lang="de">
<head>
<meta charset="utf-8">
<title>Mirela Hollmeister Kosmetikstudio – Broschüre</title>
<link href="https://fonts.googleapis.com/css2?family=Josefin+Sans:wght@300;400;600&family=Oswald:wght@200&family=Open+Sans:wght@400;600&display=swap" rel="stylesheet">
<style>
  :root{
    --navy:#34405b;
    --navy-deep:#2b3550;
    --navy-soft:#4b5872;
    --gold:#e6c05a;
    --gold-light:#f3d98a;
    --paper:#ededee;
    --ink:#343a4a;
    --stage:#e2e2e2;
    --white:#ffffff;
  }
  *{margin:0;padding:0;box-sizing:border-box}
  html,body{width:1200px;height:1153px;overflow:hidden;background:var(--stage)}
  body{position:relative;font-family:'Josefin Sans',sans-serif;color:var(--ink)}
  .spread{position:absolute;left:50px;width:1100px;height:550px;background:var(--paper);box-shadow:0 6px 14px rgba(0,0,0,.18);overflow:hidden}
  .spread--cover{top:17px}
  .spread--inside{top:586px}
  .spread svg.shapes{position:absolute;left:0;top:0}
  .fold{position:absolute;left:535px;top:0;width:30px;height:100%;background:linear-gradient(90deg,rgba(0,0,0,0) 0%,rgba(0,0,0,.10) 50%,rgba(255,255,255,.12) 52%,rgba(0,0,0,0) 100%);pointer-events:none}
  .abs{position:absolute}

  .brand{display:flex;align-items:center;justify-content:center;gap:9px;font-weight:400;font-size:21px;letter-spacing:.5px}
  .brand__dot{width:30px;height:30px;border:2px solid var(--gold);border-radius:50%;flex:none}
  .brand--light{color:var(--white)}
  .brand--dark{color:var(--navy-deep)}
  .brand-sub{font-family:'Open Sans',sans-serif;font-size:7.5px;letter-spacing:3.2px;color:var(--white);text-align:center}

  .intro{left:40px;width:470px;top:200px;text-align:center;color:var(--gold);font-weight:300;font-size:18.5px;line-height:24px}

  .location{font-family:'Open Sans',sans-serif;font-size:10px;line-height:14px;color:var(--ink)}
  .location h3{font-family:'Josefin Sans',sans-serif;font-weight:400;font-size:12px;color:var(--gold);margin-bottom:3px}
  .location p{display:flex;align-items:center;gap:5px}
  .location svg{width:8px;height:8px;fill:var(--ink)}
  .divider{left:269px;top:432px;width:1px;height:82px;background:#c9c9cc}

  .claim{left:820px;width:200px;text-align:center;color:var(--white)}
  .claim__big{top:150px;font-family:'Oswald',sans-serif;font-weight:200;font-size:46px;letter-spacing:-1px;line-height:1}
  .claim__line{top:203px;font-weight:300;font-size:20px;letter-spacing:1px}
  .claim__von{top:228px;font-weight:300;font-size:21px;display:flex;align-items:center;justify-content:center;gap:12px}
  .claim__von span.rule{display:block;width:42px;height:1px;background:var(--gold)}
  .claim__innen{top:256px;font-weight:300;font-size:38px;letter-spacing:3px}
  .pill{left:899px;top:295px;width:150px;height:15px;border-radius:8px;background:var(--gold);color:var(--white);font-size:8.5px;line-height:16px;text-align:center}

  .tagline{left:600px;width:450px;top:508px;text-align:center;font-family:'Open Sans',sans-serif;font-weight:600;font-size:7.5px;letter-spacing:.8px;color:var(--navy-deep)}

  .about__title{left:30px;width:490px;top:345px;text-align:center;color:var(--gold);font-weight:300;font-size:18px;letter-spacing:.3px}
  .about__text{left:30px;width:490px;top:380px;text-align:center;font-weight:300;font-size:15px;line-height:26px;color:var(--ink)}

  .footer-bar{left:0;top:498px;width:1100px;height:30px;background:var(--navy);display:flex}
  .footer-bar div{flex:1;display:flex;align-items:center;justify-content:center;gap:8px;color:var(--white);font-weight:300;font-size:15px;padding-top:2px}
  .footer-bar .dot{width:9px;height:9px;border:1.5px solid var(--gold);border-radius:50%}
  .footer-bar a{color:var(--gold);text-decoration:none}

  .treatment{left:612px;display:flex;align-items:center;gap:24px;font-weight:300;font-size:16.5px;color:var(--ink)}
  .treatment__photo{width:80px;height:80px;border-radius:50%;border:2px solid var(--gold);flex:none}
  .treatment__photo--eyeliner{background:radial-gradient(circle at 45% 50%,#5f8f86 0 12%,#e3cbbb 30%,#c9a792 100%)}
  .treatment__photo--brows{background:linear-gradient(180deg,#8a6a55 0%,#d7b49c 40%,#c59d82 100%)}
  .treatment__photo--lips{background:radial-gradient(ellipse at 50% 55%,#d98b84 0 35%,#e8c2b0 70%,#dcb39e 100%)}
</style>
</head>
<body>

<svg width="0" height="0" style="position:absolute" aria-hidden="true">
  <symbol id="icon-pin" viewBox="0 0 10 10"><path d="M5 0a3.5 3.5 0 0 0-3.5 3.5C1.5 6 5 10 5 10s3.5-4 3.5-6.5A3.5 3.5 0 0 0 5 0zm0 5a1.4 1.4 0 1 1 0-2.8A1.4 1.4 0 0 1 5 5z"/></symbol>
  <symbol id="icon-phone" viewBox="0 0 10 10"><path d="M2 0.5l1.8 2.2-1 1.2c.6 1.3 1.6 2.3 2.9 2.9l1.2-1 2.2 1.8-.9 1.6C4.5 9.2.8 5.5.4 1.4z"/></symbol>
  <symbol id="icon-mail" viewBox="0 0 10 10"><path d="M0 4l5-3 5 3v5H0zm1 .6V8h8V4.6L5 7z"/></symbol>
</svg>

<!-- Cover spread: back page + front page -->
<section class="spread spread--cover">
  <svg class="shapes" width="1100" height="550" viewBox="0 0 1100 550">
    <defs>
      <linearGradient id="navyFade" x1="0" y1="0" x2="0" y2="1">
        <stop offset="0" stop-color="#2c3651"/>
        <stop offset="1" stop-color="#4e5b74"/>
      </linearGradient>
      <linearGradient id="coverPortrait" x1="0" y1="0" x2="1" y2="0">
        <stop offset="0" stop-color="#c79f86"/>
        <stop offset=".45" stop-color="#e7c9b3"/>
        <stop offset=".75" stop-color="#b99c8f"/>
        <stop offset="1" stop-color="#3c4863"/>
      </linearGradient>
      <linearGradient id="goldSweep" x1="0" y1="0" x2="1" y2="0">
        <stop offset="0" stop-color="#d9ad3c"/>
        <stop offset=".5" stop-color="#f3d98a"/>
        <stop offset="1" stop-color="#e0b64a"/>
      </linearGradient>
    </defs>
    <rect x="0" y="0" width="1100" height="550" fill="url(#navyFade)"/>
    <rect class="portrait" role="img" aria-label="Porträtfoto einer jungen Frau mit natürlichem Make-up" x="550" y="0" width="320" height="440" fill="url(#coverPortrait)"/>
    <!-- back page wave -->
    <path d="M0 355 C90 326 190 314 280 318 C370 322 470 348 550 376 L550 550 L0 550Z" fill="url(#goldSweep)"/>
    <path d="M0 418 C90 372 190 343 280 340 C370 338 470 358 550 382 L550 550 L0 550Z" fill="#fff"/>
    <path d="M0 421 C90 376 190 347 280 344 C370 342 470 362 550 386 L550 550 L0 550Z" fill="var(--paper)"/>
    <!-- front page wave -->
    <path d="M760 436 C900 430 1010 398 1100 355 L1100 395 C1010 420 900 436 800 437Z" fill="url(#goldSweep)"/>
    <path d="M550 386 C650 410 750 434 850 434 C950 434 1030 418 1100 395 L1100 550 L550 550Z" fill="var(--paper)"/>
  </svg>

  <div class="abs brand brand--light" style="left:0;width:550px;top:98px">
    <span class="brand__dot"></span><span>Mirela Hollmeister</span>
  </div>
  <div class="abs brand-sub" style="left:0;width:550px;top:140px">KOSMETIKSTUDIO</div>

  <p class="abs intro">Ihr Kosmetikstudio und Beauty Salon in 1080<br>Wien Professionelles Microblading und Permanent<br>Make Up für gehobene Ansprüche</p>

  <div class="abs location" style="left:85px;top:447px">
    <h3>WIEN</h3>
    <p><svg><use href="#icon-pin"/></svg>Lerchengasse 7b/21, 1080 Wien</p>
    <p><svg><use href="#icon-phone"/></svg>01/5826107</p>
    <p><svg><use href="#icon-mail"/></svg>info@mk-hollmeister.at</p>
  </div>
  <div class="abs divider"></div>
  <div class="abs location" style="left:320px;top:447px">
    <h3>VILLACH</h3>
    <p><svg><use href="#icon-pin"/></svg>Birkenstraße 24, 9581 St. Ulrich</p>
    <p><svg><use href="#icon-phone"/></svg>0664/3158902</p>
    <p><svg><use href="#icon-mail"/></svg>info@mk-hollmeister.at</p>
  </div>

  <div class="abs claim claim__big">SCHÖNHEIT</div>
  <div class="abs claim claim__line">kommt nicht nur</div>
  <div class="abs claim claim__von"><span class="rule"></span>von<span class="rule"></span></div>
  <div class="abs claim claim__innen">innen</div>
  <div class="abs pill">www.mk-hollmeister.at</div>

  <div class="abs brand brand--dark" style="left:600px;width:450px;top:468px">
    <span class="brand__dot"></span><span>Mirela Hollmeister</span>
  </div>
  <div class="abs tagline">WAS IHNEN WERTVOLL IST, GEHÖRT IN GUTE HÄNDE</div>

  <div class="fold"></div>
</section>

<!-- Inside spread: about + treatments -->
<section class="spread spread--inside">
  <svg class="shapes" width="1100" height="550" viewBox="0 0 1100 550">
    <defs>
      <linearGradient id="eyesPhoto" x1="0" y1="0" x2="0" y2="1">
        <stop offset="0" stop-color="#e2c5b1"/>
        <stop offset=".45" stop-color="#b98f76"/>
        <stop offset=".7" stop-color="#d9b8a2"/>
        <stop offset="1" stop-color="#e9d2c2"/>
      </linearGradient>
      <linearGradient id="headerNavy" x1="0" y1="0" x2="0" y2="1">
        <stop offset="0" stop-color="#2d3752"/>
        <stop offset="1" stop-color="#45526c"/>
      </linearGradient>
      <linearGradient id="goldArc" x1="0" y1="1" x2="1" y2="0">
        <stop offset="0" stop-color="#d9ad3c"/>
        <stop offset=".6" stop-color="#f0d27a"/>
        <stop offset="1" stop-color="#dcb045"/>
      </linearGradient>
    </defs>
    <path role="img" aria-label="Nahaufnahme von Augen mit Augenbrauen Permanent Makeup" d="M0 0 L598 0 C588 110 490 250 310 290 C200 303 90 300 0 297Z" fill="url(#eyesPhoto)"/>
    <path d="M0 299 C90 302 200 305 310 292 C490 252 590 110 602 0" fill="none" stroke="#fff" stroke-width="4"/>
    <path d="M0 304 C90 307 200 309 312 296 C494 256 596 112 610 0" fill="none" stroke="url(#goldArc)" stroke-width="5"/>
    <path d="M622 0 L1100 0 L1100 118 C1000 163 900 185 790 186 C700 187 625 172 572 152 C600 105 616 55 622 0Z" fill="url(#headerNavy)"/>
    <path d="M700 186 C860 192 1000 168 1100 112 L1100 140 C1000 182 870 196 760 193Z" fill="url(#goldArc)"/>
    <circle cx="270" cy="277" r="42" fill="var(--paper)" fill-opacity=".25" stroke="url(#goldArc)" stroke-width="4"/>
  </svg>

  <div class="abs brand brand--light" style="left:580px;width:500px;top:65px">
    <span class="brand__dot"></span><span>Mirela Hollmeister</span>
  </div>
  <div class="abs brand-sub" style="left:580px;width:500px;top:107px">KOSMETIKSTUDIO</div>

  <h2 class="abs about__title">IHR KOSMETIKSTUDIO UND BEAUTY SALON</h2>
  <p class="abs about__text">Für Frau Hollmeister ist Permanent Makeup ein Kunsthandwerk.<br>Das Team von MK-Hollmeister ist spezialisiert auf natürliches<br>Permanent Makeup damit der individuelle Typ jeder Kundin am<br>schönsten zum Ausdruck kommt.</p>

  <div class="abs treatment" style="top:205px">
    <div class="treatment__photo treatment__photo--eyeliner" role="img" aria-label="Foto eines Auges mit Lidstrich"></div>
    <span>Lidstrich Permanent Makeup (eyeliner)</span>
  </div>
  <div class="abs treatment" style="top:297px">
    <div class="treatment__photo treatment__photo--brows" role="img" aria-label="Foto einer Augenbraue"></div>
    <span>Augenbrauen Permanent Makeup (eyebrows2)</span>
  </div>
  <div class="abs treatment" style="top:389px">
    <div class="treatment__photo treatment__photo--lips" role="img" aria-label="Foto von Lippen nach Lip Blushing"></div>
    <span>Lip Blushing (lips)</span>
  </div>

  <div class="abs footer-bar">
    <div>Online Termin vereinbaren <span class="dot"></span> <a href="#">www.mk-hollmeister.at</a></div>
    <div>Online Termin vereinbaren <span class="dot"></span> <a href="#">www.mk-hollmeister.at</a></div>
  </div>

  <div class="fold"></div>
</section>

</body>
</html>
```